Fenwell Building Partners Stationary Revamp

We need a full set of new stationary including business cards for our Public Sector Construction company based in the South East of England. We have a new logo (attached) that we want to launch and revamp all of our company literature. We are required to send a lot of correspondence to residents etc so a consistent theme is required across everything. Also attached is our existing templates.

Target Market(s)

We work for Council and government provided housing organisations and NOT private individuals. All of our clients represent government spent money, so we need to look professional and instantly recognisable brand.

Industry/Entity Type

Business

Colors

Designer to choose colors to be used in the design.

Requirements
Must have
• New fresh designs that utilise our new logo. And the letterhead needs to be able to be rolled out onto a word template so that all staff can type straight onto it rather than us having to have it printed first.
Nice to have
• I am looking forward to seeing your best efforts as designers.

```html
<!DOCTYPE html>
<html lang="en">
<head>
<meta charset="utf-8">
<title>Fenwell Building Partners – Business Card</title>
<link href="https://fonts.googleapis.com/css2?family=Open+Sans:wght@400;600;700&display=swap" rel="stylesheet">
<style>
  :root {
    --backdrop: #3b3431;
    --card: #141414;
    --card-edge: #1f1f1f;
    --ink: #f2f2f2;
    --ink-soft: #d8d8d8;
    --muted: #8a8a8a;
    --gold: #d9a520;
    --rule: #bdbdbd;
  }
  * { box-sizing: border-box; margin: 0; padding: 0; }
  html, body { width: 1200px; height: 864px; overflow: hidden; }
  body {
    background: var(--backdrop);
    font-family: "Open Sans", Arial, sans-serif;
    display: flex;
    align-items: center;
    justify-content: center;
    gap: 54px;
  }
  .card {
    width: 520px;
    height: 300px;
    background: var(--card);
    border: 1px solid var(--card-edge);
    position: relative;
    box-shadow: 0 10px 30px rgba(0,0,0,.45);
  }

  /* Back side */
  .card--back {
    display: flex;
    flex-direction: column;
    align-items: center;
    justify-content: center;
  }
  .card--back .brand-name {
    color: var(--muted);
    font-size: 24px;
    font-weight: 600;
  }
  .card--back .brand-since {
    color: var(--muted);
    font-size: 9px;
    letter-spacing: 2px;
    margin-top: 6px;
  }
  .card--back .website {
    color: var(--muted);
    font-size: 13px;
    letter-spacing: 2.5px;
    margin-top: 40px;
  }

  /* Front side */
  .card--front {
    display: flex;
    align-items: center;
  }
  .brand-block {
    width: 286px;
    padding-left: 30px;
    display: flex;
    flex-direction: column;
    align-items: flex-start;
  }
  .brand-block .brand-mark {
    width: 18px;
    height: 18px;
    border-radius: 50%;
    background: var(--gold);
    margin-bottom: 14px;
  }
  .brand-block .brand-name {
    color: var(--ink);
    font-size: 22px;
    font-weight: 600;
    line-height: 1.2;
  }
  .brand-block .brand-since {
    color: var(--ink-soft);
    font-size: 9px;
    letter-spacing: 2px;
    margin-top: 10px;
    padding-top: 6px;
    border-top: 1px solid var(--rule);
    width: 200px;
    text-align: center;
  }
  .divider {
    width: 1px;
    height: 220px;
    background: var(--rule);
  }
  .contact-block {
    padding-left: 22px;
    color: var(--ink-soft);
    font-size: 12.5px;
    line-height: 1.35;
  }
  .person-name {
    color: var(--gold);
    font-weight: 700;
    font-size: 15px;
  }
  .person-role {
    color: var(--ink);
    font-size: 14px;
    margin-bottom: 8px;
  }
  .address { margin-bottom: 4px; }
  .contact-line {
    display: flex;
    align-items: center;
    gap: 6px;
  }
  .contact-line svg { width: 11px; height: 11px; fill: var(--gold); flex: none; }
  .reg-no { margin-top: 2px; }
</style>
</head>
<body>
  <section class="card card--back">
    <div class="brand-name">Fenwell Building Partners</div>
    <div class="brand-since">SINCE 1944</div>
    <div class="website">www.fenwellbuilding.co.uk</div>
  </section>

  <section class="card card--front">
    <div class="brand-block">
      <span class="brand-mark"></span>
      <div class="brand-name">Fenwell Building<br>Partners</div>
      <div class="brand-since">SINCE 1944</div>
    </div>
    <div class="divider"></div>
    <div class="contact-block">
      <div class="person-name">R J MARLOW MIOD</div>
      <div class="person-role">MANAGING DIRECTOR</div>
      <div class="address">Harlow House<br>12 Ashgrove Road<br>Dartford, Kent, DA1 3QP</div>
      <div class="contact-line">
        <svg viewBox="0 0 12 12" aria-hidden="true"><path d="M2.5 1l2 2.3-1 1.2a7 7 0 0 0 4 4l1.2-1 2.3 2-1.3 1.5C5.5 10.8 1.2 6.5 1 2.3z"/></svg>
        020 7946 0123
      </div>
      <div class="contact-line">
        <svg viewBox="0 0 12 12" aria-hidden="true"><rect x="3" y="1" width="6" height="3"/><rect x="1" y="4.5" width="10" height="5" rx="1"/><rect x="3" y="8" width="6" height="3"/></svg>
        020 7946 0124
      </div>
      <div class="contact-line">
        <svg viewBox="0 0 12 12" aria-hidden="true"><path d="M1 2.5h10v7H1z M1.5 3l4.5 3.5L10.5 3" stroke="#141414" stroke-width=".8"/></svg>
        info@fenwellbuilding.co.uk
      </div>
      <div class="contact-line">
        <svg viewBox="0 0 12 12" aria-hidden="true"><circle cx="6" cy="6" r="5"/><path d="M1 6h10M6 1c-2.5 3-2.5 7 0 10M6 1c2.5 3 2.5 7 0 10" stroke="#141414" stroke-width=".7" fill="none"/></svg>
        www.fenwellbuilding.co.uk
      </div>
      <div class="reg-no">Reg No: 09182736</div>
    </div>
  </section>
</body>
</html>
```